Create a pouch design for a new sports supplement product

Dimensions are 235mm (width) x 335mm (length) x 110mm (gusset)
File 1 - Extension of design brief please read both briefs
File 2 - Is 2 potential pouches this is just to give you a better example of size the dimensions are for the pouch on the right. This picture is not to give you design ideas as I am not very keen on either of these designs.
We need a design to be printed onto the pouches of our whey protein product. The brand name is 'Brisk Fuelworks' and needs to be displayed on the packaging either just writing or a simple logo design. I am not the most creative person in the world but have put together a more detailed brief listing some of the key information that needs to be included on the pouch (See attachment) Please feel free if you have experience of this the sports supplement market or have different ideas then please feel free to explore them.
The pouch would either be printed straight onto the pouch, or possibly just a printed label (front & back) to be stuck onto the pouch. Please design either or both.
Open to different colour schemes. Design has to be modern looking and eye-catching.
Some key points;
High quality whey protein concentrate
All Natural
Soy free
Great tasting
Please google image search 'protein pouches' to see other designs if your not familiar with the sports supplement market.
Any questions feel free to ask.
Updates
Project Deadline Extended
Reason: give me chance to give feedback
Hi, Thanks for all your design! I am really busy at the moment so haven't had chance to give feedback and have a proper look through all the designs. I have extended the time frame to give myself chance to give proper feedback and see any changes needed. Expect feedback sunday at the latest, and I will be pick a design early next week.
Target Market(s)
Sports supplement market. Product is a whey protein shake
Industry/Entity Type
Nutrition
Look and feel
Each slider illustrates characteristics of the customer's brand and the style your logo design should communicate.

```html
<!DOCTYPE html>
<html lang="en">
<head>
<meta charset="utf-8">
<title>Brisk Fuelworks – Natural Whey Protein Pouch</title>
<link href="https://fonts.googleapis.com/css2?family=Anton&family=Arimo:ital,wght@0,400;1,700&display=swap" rel="stylesheet">
<style>
  :root {
    --page: #ffffff;
    --pouch-black: #0b0506;
    --glow-red: #9a1a0c;
    --glow-orange: #e0641a;
    --glow-core: #fff3c4;
    --brand-yellow: #f7d52a;
    --text-white: #ffffff;
    --text-grey: #d8d8d8;
    --pill-red: #d8221f;
    --arrow-amber: #f2b01c;
  }
  * { box-sizing: border-box; margin: 0; padding: 0; }
  html, body { width: 1070px; height: 1200px; overflow: hidden; background: var(--page); }
  .canvas { position: relative; width: 1070px; height: 1200px; }

  .pouch {
    position: absolute;
    left: 140px; top: 30px; width: 790px; height: 1150px;
    background:
      radial-gradient(ellipse 90px 60px at 48% 53%, var(--glow-core) 0%, rgba(255,220,120,0.6) 45%, rgba(255,160,40,0) 100%),
      radial-gradient(ellipse 420px 330px at 50% 46%, var(--glow-orange) 0%, var(--glow-red) 40%, rgba(60,8,6,0.6) 70%, rgba(11,5,6,0) 100%),
      var(--pouch-black);
    clip-path: polygon(0 0, 100% 0, 100% 8.6%, 98.2% 9.3%, 100% 10%, 100% 100%, 0 100%, 0 10%, 1.8% 9.3%, 0 8.6%);
    font-family: "Arimo", Arial, sans-serif;
    color: var(--text-white);
  }

  .tear-note {
    position: absolute; right: 58px; top: 70px;
    font-size: 13px; display: flex; align-items: center; gap: 8px;
  }
  .tear-note svg { width: 10px; height: 12px; }

  .brand {
    position: absolute; left: 0; right: 0; top: 300px;
    text-align: center;
    font-family: "Anton", Impact, sans-serif;
    font-weight: 400;
    color: var(--brand-yellow);
    line-height: 1;
  }
  .brand-line-top { display: block; font-size: 180px; letter-spacing: 4px; }
  .brand-line-bottom { display: block; font-size: 104px; letter-spacing: 3px; margin-top: 6px; }

  .product-type {
    position: absolute; left: 0; right: 0; top: 604px;
    text-align: center; font-size: 30px; font-style: italic; font-weight: 700;
  }

  .flavour-pill {
    position: absolute; left: 234px; top: 728px; width: 322px; height: 62px;
    background: var(--pill-red); border-radius: 16px;
    display: flex; align-items: center; justify-content: center;
    font-size: 30px; font-style: italic; font-weight: 700;
  }

  .benefits {
    position: absolute; left: 0; right: 0; top: 870px;
    list-style: none; text-align: center;
    font-size: 21px; font-style: italic; font-weight: 700; line-height: 39px;
  }

  .net-weight {
    position: absolute; left: 0; right: 0; top: 1034px;
    text-align: center; font-size: 18px; color: var(--text-grey);
  }
</style>
</head>
<body>
<div class="canvas">
  <div class="pouch">
    <div class="tear-note">Tear here and Reseal
      <svg viewBox="0 0 10 12" aria-hidden="true"><polygon points="0,0 10,6 0,12" fill="var(--arrow-amber)"/></svg>
    </div>

    <h1 class="brand">
      <span class="brand-line-top">BRISK</span>
      <span class="brand-line-bottom">FUELWORKS</span>
    </h1>

    <p class="product-type">Natural Whey Protein</p>

    <div class="flavour-pill">Strawberry Flavour</div>

    <ul class="benefits">
      <li>No artificial Flavours</li>
      <li>Excellent Amino acid profile</li>
      <li>80% high quality protein content</li>
      <li>Soy free</li>
    </ul>

    <p class="net-weight">909g 30 servings</p>
  </div>
</div>
</body>
</html>
```